Business Card Design

Brindle Creek Mowers was established in 1953, now under new ownership, new ownership since July 2014. We service, repair, and provide parts for all brands of outdoor power equipment. As a full service small engine repair shop we work on lawn mowers, chainsaws, weed-eaters, blowers, sprayers, pole-saws, hedge trimmers, edgers, riding mowers, zero-turn mowers, generators, and pressure washers in South Florida, Hollywood, Pembroke Pines, Miami, and surrounding areas. Catering to lawn professionals, aborists, as well as residential customers.

Brindle Creek Mowers has some of the finest equipment lines you'll find in South Florida and we back our products with outstanding service, parts, friendly staff and highly trained & certified technicians. The customer is top priority when it comes to Brindle Creek Mowers and we strive to provide the best possible experience when you visit our shop.

We sell also sell new commercial and residential lawn equipment including KORVA, Gladwin, and VELK.

We'd like the final design to communicate

Industry/Entity Type

Business

Contact Information for Business Card

Brindle Creek Mowers
4826 Marlow Blvd
Larkspur FL 33187
ph: 954-627-1583
email:brindlecreekmowers@mailora.net
url: www.brindlecreekmowers-example.com

```html
<!DOCTYPE html>
<html lang="en">
<head>
<meta charset="utf-8">
<title>Brindle Creek Mowers – Business Card</title>
<link rel="stylesheet" href="https://fonts.googleapis.com/css2?family=Ubuntu:wght@500;700&family=Roboto:wght@300;400&display=swap">
<style>
  :root {
    --page: #ececec;
    --card-white: #ffffff;
    --brand-green: #1fb868;
    --green-deep: #0f9d55;
    --green-light: #27c477;
    --ink-dark: #3a3a3a;
    --ink-soft: #555555;
    --rule: #2bbf72;
  }
  * { box-sizing: border-box; margin: 0; padding: 0; }
  html, body { width: 1200px; height: 885px; overflow: hidden; }
  body {
    background: var(--page);
    display: flex;
    flex-direction: column;
    align-items: center;
    justify-content: center;
    gap: 44px;
    font-family: "Roboto", Arial, sans-serif;
  }
  .card {
    width: 560px;
    height: 320px;
    border-radius: 18px;
    box-shadow: 0 6px 18px rgba(0,0,0,0.12);
    position: relative;
    overflow: hidden;
  }
  /* Front */
  .card-front {
    background: var(--card-white);
    display: flex;
    align-items: center;
  }
  .brand-block {
    width: 250px;
    padding-left: 40px;
    font-family: "Ubuntu", Arial, sans-serif;
    font-weight: 700;
    line-height: 1.05;
  }
  .brand-block .brand-top { color: var(--brand-green); font-size: 30px; display: block; }
  .brand-block .brand-bottom { color: var(--ink-dark); font-size: 30px; display: block; padding-left: 56px; }
  .divider {
    width: 1.5px;
    height: 220px;
    background: linear-gradient(to bottom, rgba(43,191,114,0), var(--rule) 30%, var(--rule) 70%, rgba(43,191,114,0));
  }
  .details { padding-left: 26px; color: var(--ink-soft); }
  .person-name {
    font-family: "Ubuntu", Arial, sans-serif;
    font-weight: 700;
    font-size: 25px;
    color: var(--brand-green);
  }
  .person-title { font-size: 14px; font-weight: 300; margin-top: 2px; margin-bottom: 20px; }
  .address { font-size: 13px; font-weight: 300; line-height: 1.35; margin-bottom: 14px; }
  .contact-list { list-style: none; font-size: 13px; font-weight: 300; }
  .contact-list li { display: flex; align-items: center; gap: 8px; margin-bottom: 4px; }
  .contact-icon { width: 15px; height: 15px; flex: none; }
  /* Back */
  .card-back {
    background: linear-gradient(135deg, var(--green-light) 0%, var(--brand-green) 45%, var(--green-deep) 100%);
    display: flex;
    align-items: center;
    justify-content: center;
  }
  .back-brand {
    font-family: "Ubuntu", Arial, sans-serif;
    font-weight: 700;
    font-size: 38px;
    color: var(--card-white);
    letter-spacing: 0.5px;
  }
</style>
</head>
<body>

  <section class="card card-front">
    <div class="brand-block">
      <span class="brand-top">Brindle Creek</span>
      <span class="brand-bottom">Mowers</span>
    </div>
    <div class="divider"></div>
    <div class="details">
      <div class="person-name">Employee Name</div>
      <div class="person-title">Managing Director</div>
      <div class="address">4826 Marlow Blvd<br>Larkspur FL 33187</div>
      <ul class="contact-list">
        <li>
          <svg class="contact-icon" viewBox="0 0 16 16" aria-hidden="true">
            <rect width="16" height="16" rx="2" fill="#1fb868"/>
            <path d="M5 3.5h2l1 2.5-1.3 1a6 6 0 0 0 2.3 2.3l1-1.3 2.5 1v2a1 1 0 0 1-1 1A8.5 8.5 0 0 1 4 4.5a1 1 0 0 1 1-1z" fill="#fff"/>
          </svg>
          954-627-1583
        </li>
        <li>
          <svg class="contact-icon" viewBox="0 0 16 16" aria-hidden="true">
            <rect width="16" height="16" rx="2" fill="#1fb868"/>
            <rect x="3" y="4.5" width="10" height="7" fill="none" stroke="#fff" stroke-width="1.2"/>
            <path d="M3 4.5l5 4 5-4" fill="none" stroke="#fff" stroke-width="1.2"/>
          </svg>
          brindlecreekmowers@mailora.net
        </li>
        <li>
          <svg class="contact-icon" viewBox="0 0 16 16" aria-hidden="true">
            <rect width="16" height="16" rx="2" fill="#1fb868"/>
            <circle cx="8" cy="8" r="4.8" fill="none" stroke="#fff" stroke-width="1.1"/>
            <ellipse cx="8" cy="8" rx="2" ry="4.8" fill="none" stroke="#fff" stroke-width="1"/>
            <path d="M3.2 8h9.6" stroke="#fff" stroke-width="1"/>
          </svg>
          www.brindlecreekmowers-example.com
        </li>
      </ul>
    </div>
  </section>

  <section class="card card-back">
    <div class="back-brand">Brindle Creek Mowers</div>
  </section>

</body>
</html>
```